Präsentationsvorlagen für Verwaltungsfirma
Zielgruppe
Verwaltungsfirma, IT-Dienstleistungen, Rechnungswesen
Aufgabenstellung
Benötigen Powerpoint Vorlage im Design unserer Farben. inkl. Logo
Benötige das Power Point Format - .pptx

```html
<!DOCTYPE html>
<html lang="de">
<head>
<meta charset="utf-8">
<title>Nord &amp; Kollegen – Präsentationsvorlage</title>
<link rel="stylesheet" href="https://fonts.googleapis.com/css2?family=Sora:wght@400;600;700&family=Unbounded:wght@700&display=swap">
<style>
  :root{
    --navy:#1a4f9f;
    --blue:#1f6fd0;
    --sky:#27bcf8;
    --pale:#d6effc;
    --paler:#eef8fe;
    --ink:#2b2f3a;
    --stage:#a8a8a8;
  }
  *{box-sizing:border-box;margin:0;padding:0}
  html,body{width:1200px;height:2317px;overflow:hidden}
  body{background:var(--stage);position:relative;font-family:"Sora",sans-serif}
  .slide{position:absolute;left:148px;width:1008px;height:568px;transform:scale(.9);transform-origin:0 0;
    overflow:hidden;background:#fff;box-shadow:0 6px 14px rgba(0,0,0,.35)}
  .slide--title{top:99px}
  .slide--intro{top:634px}
  .slide--services{top:1170px}
  .slide--contact{top:1709px}
  .slide svg.bg{position:absolute;inset:0;width:1008px;height:568px}
  .brand{position:absolute;font-family:"Sora",sans-serif;font-weight:700;color:var(--navy);letter-spacing:-.5px;white-space:nowrap}
  .brand--lg{left:90px;top:112px;font-size:29px}
  .brand--sm{left:68px;top:58px;font-size:20px}
  .headline{position:absolute;font-family:"Unbounded",sans-serif;font-weight:700;color:#fff}
  .slide--title .headline{left:0;width:780px;top:226px;text-align:center;font-size:47px;line-height:56px}
  .slide--contact .headline{left:80px;top:228px;font-size:37px;line-height:42px}
  .lead{position:absolute;left:80px;top:326px;color:#fff;font-size:16px}
  .url{position:absolute;left:86px;top:484px;font-size:35px;font-weight:700;color:#fff}
  .intro-text{position:absolute;left:406px;top:62px;width:448px;color:#fff;font-size:13.4px;font-weight:600;line-height:20px}
  .section-title{position:absolute;left:134px;top:30px;color:#fff;font-size:34px;font-weight:700}
  .service{position:absolute;top:262px;width:230px}
  .service__label{margin:0 auto;width:210px;height:31px;border-radius:16px;background:var(--sky);color:#fff;
    font-weight:700;font-size:15.5px;text-align:center;line-height:31px;position:relative}
  .service__label::after{content:"";position:absolute;left:50%;bottom:-8px;margin-left:-8px;border:8px solid transparent;border-bottom:0;border-top-color:var(--sky)}
  .service__list{list-style:none;margin-top:37px;display:flex;flex-direction:column;gap:16px}
  .service__list li{position:relative;padding-left:24px;font-size:14.6px;line-height:17px;color:var(--ink)}
  .service__list li::before{content:"";position:absolute;left:4px;top:2px;width:10px;height:10px;border-radius:50%;background:var(--sky)}
  .service--building{left:119px}
  .service--finance{left:387px}
  .service--it{left:655px}
  .contact-item{position:absolute;left:663px;width:269px;height:108px;text-align:center;color:#fff;font-weight:700;font-size:15.5px;line-height:19px;
    display:flex;align-items:flex-end;justify-content:center;padding-bottom:24px}
  .contact-item--1{top:69px}
  .contact-item--2{top:231px;padding-bottom:14px}
  .contact-item--3{top:393px}
</style>
</head>
<body>

<section class="slide slide--title">
  <svg class="bg" viewBox="0 0 1008 568">
    <defs>
      <linearGradient id="t-blue" x1="0" x2="1"><stop offset="0" stop-color="#1d5fb8"/><stop offset="1" stop-color="#18479a"/></linearGradient>
      <linearGradient id="t-sky" x1="0" x2="1"><stop offset="0" stop-color="#8fe0ff"/><stop offset=".5" stop-color="#2bbdf8"/><stop offset="1" stop-color="#27b7f5"/></linearGradient>
      <linearGradient id="t-pale" x1="0" x2="1"><stop offset="0" stop-color="#bfe8fd"/><stop offset="1" stop-color="#e8f7ff"/></linearGradient>
      <linearGradient id="t-photo" x1="0" y1="0" x2="0" y2="1"><stop offset="0" stop-color="#7fa36a"/><stop offset=".45" stop-color="#6f8fae"/><stop offset=".7" stop-color="#2f6fd6"/><stop offset="1" stop-color="#8a9b7a"/></linearGradient>
    </defs>
    <polygon points="0,0 372,0 408,48 0,48" fill="url(#t-pale)"/>
    <polygon points="0,548 1008,548 1008,568 0,568" fill="url(#t-sky)"/>
    <polygon points="410,0 1008,0 1008,532 425,532 560,362 572,215" fill="url(#t-photo)" role="img" aria-label="Luftbild des Bürogebäudes mit See und Parkplatz"/>
    <polygon points="0,202 700,202 753,283 700,365 0,365" fill="url(#t-blue)"/>
    <polygon points="0,380 530,380 520,396 0,396" fill="var(--blue)"/>
    <polygon points="0,468 420,468 372,540 0,540" fill="url(#t-sky)"/>
    <polygon points="436,468 462,468 412,540 386,540" fill="var(--sky)"/>
  </svg>
  <div class="brand brand--lg">Nord &amp; Kollegen GmbH</div>
  <h1 class="headline">Burogemeinschaft<br>in Halden</h1>
  <div class="url">nordkollegen.at</div>
</section>

<section class="slide slide--intro">
  <svg class="bg" viewBox="0 0 1008 568">
    <defs>
      <linearGradient id="i-blue" x1="0" x2="1"><stop offset="0" stop-color="#18479a"/><stop offset="1" stop-color="#1f6fd0"/></linearGradient>
      <linearGradient id="i-photo" x1="0" x2="1"><stop offset="0" stop-color="#6f8a6a"/><stop offset=".45" stop-color="#a58a68"/><stop offset="1" stop-color="#c8ccd2"/></linearGradient>
    </defs>
    <polygon points="0,100 0,568 210,568" fill="var(--pale)" opacity=".8"/>
    <polygon points="404,0 1008,0 850,238 290,238 70,568 0,568" fill="url(#i-blue)"/>
    <polygon points="290,238 960,238 960,568 70,568" fill="url(#i-photo)" role="img" aria-label="Besprechungsraum mit Tischen, Stühlen und Fensterfront zum See"/>
    <polygon points="1008,100 1008,568 775,568" fill="var(--pale)" opacity=".85"/>
    <polygon points="1008,370 1008,568 870,568" fill="var(--sky)"/>
    <g fill="var(--sky)">
      <circle cx="100" cy="198" r="1.6"/><circle cx="118" cy="198" r="1.6"/><circle cx="136" cy="198" r="1.6"/><circle cx="154" cy="198" r="1.6"/><circle cx="172" cy="198" r="1.6"/>
      <circle cx="118" cy="213" r="1.6"/><circle cx="136" cy="213" r="1.6"/><circle cx="154" cy="213" r="1.6"/><circle cx="172" cy="213" r="1.6"/><circle cx="190" cy="213" r="1.6"/>
      <circle cx="136" cy="228" r="1.6"/><circle cx="154" cy="228" r="1.6"/><circle cx="172" cy="228" r="1.6"/><circle cx="190" cy="228" r="1.6"/><circle cx="208" cy="228" r="1.6"/>
    </g>
  </svg>
  <div class="brand brand--sm">Nord &amp; Kollegen GmbH</div>
  <p class="intro-text">Wir, die Nord &amp; Kollegen GmbH, sind eine renommierte Firmengruppe in Halden (Bezirk Nordtal) und bieten neben der Gebäudeverwaltung eine Vielzahl zentraler Dienstleistungen an diesem Standort an. Mit unserem umfangreichen Leistungsspektrum tragen wir dazu bei, die Geschäftsprozesse unserer Kund:innen reibungslos und effizient zu gestalten.</p>
</section>

<section class="slide slide--services">
  <svg class="bg" viewBox="0 0 1008 568">
    <defs>
      <linearGradient id="s-blue" x1="0" x2="1"><stop offset="0" stop-color="#1a4f9f"/><stop offset="1" stop-color="#1f6fd0"/></linearGradient>
      <linearGradient id="s-pale" x1="0" x2="1"><stop offset="0" stop-color="#c2e9fd"/><stop offset="1" stop-color="#e8f7ff"/></linearGradient>
      <linearGradient id="s-icon" x1="0" y1="0" x2="0" y2="1"><stop offset="0" stop-color="#1f6fd0"/><stop offset="1" stop-color="#18479a"/></linearGradient>
    </defs>
    <polygon points="569,0 1008,0 1008,47 600,47" fill="url(#s-pale)"/>
    <polygon points="0,150 0,568 270,568" fill="var(--paler)"/>
    <polygon points="1008,320 1008,568 835,568" fill="var(--pale)"/>
    <polygon points="1008,445 1008,568 920,568" fill="var(--sky)"/>
    <polygon points="0,0 489,0 559,98 0,98" fill="url(#s-blue)"/>
    <polygon points="507,0 544,0 602,98 565,98" fill="var(--navy)"/>
    <g fill="var(--sky)">
      <circle cx="855" cy="92" r="1.6"/><circle cx="871" cy="92" r="1.6"/><circle cx="887" cy="92" r="1.6"/><circle cx="903" cy="92" r="1.6"/><circle cx="919" cy="92" r="1.6"/>
      <circle cx="871" cy="107" r="1.6"/><circle cx="887" cy="107" r="1.6"/><circle cx="903" cy="107" r="1.6"/><circle cx="919" cy="107" r="1.6"/><circle cx="935" cy="107" r="1.6"/>
      <circle cx="887" cy="122" r="1.6"/><circle cx="903" cy="122" r="1.6"/><circle cx="919" cy="122" r="1.6"/><circle cx="935" cy="122" r="1.6"/><circle cx="951" cy="122" r="1.6"/>
    </g>
    <line x1="234" y1="187" x2="770" y2="187" stroke="var(--sky)" stroke-width="2"/>
    <g stroke="var(--sky)" stroke-width="1.5" stroke-dasharray="5 4"><line x1="374" y1="193" x2="374" y2="470"/><line x1="636" y1="193" x2="636" y2="470"/></g>
    <g fill="#fff" stroke="var(--sky)" stroke-width="2"><circle cx="374" cy="187" r="6"/><circle cx="636" cy="187" r="6"/></g>
    <g fill="url(#s-icon)" stroke="var(--sky)" stroke-width="5">
      <circle cx="234" cy="187" r="56"/><circle cx="502" cy="187" r="56"/><circle cx="770" cy="187" r="56"/>
    </g>
    <g fill="none" stroke="#fff" stroke-width="4"><circle cx="234" cy="187" r="50"/><circle cx="502" cy="187" r="50"/><circle cx="770" cy="187" r="50"/></g>
    <g fill="#fff">
      <rect x="214" y="162" width="40" height="47"/>
      <g fill="var(--navy)">
        <rect x="220" y="168" width="6" height="6"/><rect x="231" y="168" width="6" height="6"/><rect x="242" y="168" width="6" height="6"/>
        <rect x="220" y="179" width="6" height="6"/><rect x="231" y="179" width="6" height="6"/><rect x="242" y="179" width="6" height="6"/>
        <rect x="220" y="190" width="6" height="6"/><rect x="242" y="190" width="6" height="6"/>
        <rect x="229" y="196" width="10" height="13"/>
      </g>
    </g>
    <g>
      <rect x="484" y="161" width="36" height="50" rx="5" fill="#fff"/>
      <rect x="490" y="167" width="24" height="10" fill="var(--navy)"/>
      <g fill="var(--navy)">
        <rect x="490" y="182" width="6" height="5"/><rect x="499" y="182" width="6" height="5"/><rect x="508" y="182" width="6" height="5"/>
        <rect x="490" y="191" width="6" height="5"/><rect x="499" y="191" width="6" height="5"/><rect x="508" y="191" width="6" height="5"/>
        <rect x="490" y="200" width="6" height="5"/><rect x="499" y="200" width="15" height="5"/>
      </g>
    </g>
    <g fill="none" stroke="#fff" stroke-width="4" stroke-linejoin="round">
      <path d="M752 176 L788 176 L796 190 L796 204 L744 204 L744 190 Z"/>
      <line x1="744" y1="190" x2="796" y2="190"/>
    </g>
    <g fill="#fff"><circle cx="781" cy="197" r="2.5"/><circle cx="789" cy="197" r="2.5"/></g>
  </svg>
  <h2 class="section-title">Unsere Leistungen</h2>
  <div class="service service--building">
    <div class="service__label">Gebäudeverwaltung</div>
    <ul class="service__list">
      <li>Bereitstellung einer modernen Infrastruktur</li>
      <li>Facility Management-Services</li>
      <li>Fuhrparkmanagement</li>
      <li>Feste &amp; Veranstaltungen</li>
    </ul>
  </div>
  <div class="service service--finance">
    <div class="service__label">Rechnungswesen</div>
    <ul class="service__list">
      <li>Buchhaltung &amp; Bilanzierung</li>
      <li>Lohn- und Gehaltsabrechnung</li>
      <li>Kostenrechnung &amp; Budgetierung</li>
      <li>Managementreports</li>
    </ul>
  </div>
  <div class="service service--it">
    <div class="service__label">Informationstechnik</div>
    <ul class="service__list">
      <li>zentrales Rechenzentrum</li>
      <li>Beschaffung, Betreuung und Weiterentwicklung des EDV-Netzwerks</li>
      <li>Hard- und Software-Support</li>
      <li>Telekommunikation</li>
    </ul>
  </div>
</section>

<section class="slide slide--contact">
  <svg class="bg" viewBox="0 0 1008 568">
    <defs>
      <linearGradient id="c-blue" x1="0" x2="1"><stop offset="0" stop-color="#1d5fb8"/><stop offset="1" stop-color="#18479a"/></linearGradient>
      <linearGradient id="c-sky" x1="0" x2="1"><stop offset="0" stop-color="#8fe0ff"/><stop offset=".5" stop-color="#2bbdf8"/><stop offset="1" stop-color="#27b7f5"/></linearGradient>
      <linearGradient id="c-pale" x1="0" x2="1"><stop offset="0" stop-color="#bfe8fd"/><stop offset="1" stop-color="#e8f7ff"/></linearGradient>
      <linearGradient id="c-dark" x1="0" y1="0" x2="1" y2="1"><stop offset="0" stop-color="#1a4fa0"/><stop offset="1" stop-color="#1b57b0"/></linearGradient>
    </defs>
    <polygon points="0,0 372,0 408,48 0,48" fill="url(#c-pale)"/>
    <polygon points="0,548 1008,548 1008,568 0,568" fill="url(#c-sky)"/>
    <polygon points="410,0 1008,0 1008,532 425,532 632,283" fill="url(#c-dark)" role="img" aria-label="abgedunkeltes Luftbild des Bürogebäudes"/>
    <polygon points="0,204 532,204 590,283 532,366 0,366" fill="url(#c-blue)"/>
    <polygon points="0,380 530,380 520,396 0,396" fill="var(--blue)"/>
    <polygon points="0,468 420,468 372,540 0,540" fill="url(#c-sky)"/>
    <polygon points="436,468 462,468 412,540 386,540" fill="var(--sky)"/>
    <g fill="none" stroke="var(--sky)" stroke-width="3">
      <rect x="663" y="69" width="269" height="108" rx="10"/>
      <rect x="663" y="231" width="269" height="108" rx="10"/>
      <rect x="663" y="393" width="269" height="108" rx="10"/>
    </g>
    <g fill="#fff" stroke="var(--sky)" stroke-width="4">
      <circle cx="797" cy="73" r="40"/><circle cx="797" cy="235" r="40"/><circle cx="797" cy="397" r="40"/>
    </g>
    <g fill="var(--navy)"><circle cx="797" cy="73" r="31"/><circle cx="797" cy="235" r="31"/><circle cx="797" cy="397" r="31"/></g>
    <path d="M797 90 C789 80 784 73 784 66 A13 13 0 0 1 810 66 C810 73 805 80 797 90 Z" fill="#fff"/>
    <circle cx="797" cy="66" r="5" fill="var(--navy)"/>
    <circle cx="797" cy="235" r="15" fill="#fff"/>
    <path d="M790 227 C789 232 795 242 803 244 L806 240 L801 237 L799 239 C797 238 794 235 793 232 L795 230 L792 225 Z" fill="var(--navy)"/>
    <circle cx="797" cy="397" r="15" fill="#fff"/>
    <rect x="788" y="391" width="18" height="12" rx="1.5" fill="none" stroke="var(--navy)" stroke-width="2"/>
    <path d="M788 392 L797 399 L806 392" fill="none" stroke="var(--navy)" stroke-width="2"/>
  </svg>
  <div class="brand brand--lg">Nord &amp; Kollegen GmbH</div>
  <h2 class="headline">Sie wollen mehr<br>wissen</h2>
  <p class="lead">Für nähere Infos bitten wir um Kontaktaufnahme.</p>
  <div class="url">nordkollegen.at</div>
  <div class="contact-item contact-item--1">+43 7000 41280</div>
  <div class="contact-item contact-item--2">Lindenweg 12, 4000<br>Halden</div>
  <div class="contact-item contact-item--3">service[AT]nordkollegen.at</div>
</section>

</body>
</html>
```